New, modern business card for growing audiology practice

We need a new business card for our audiology practice. Our logo and website have recently changed (more modern) and we want our business cards to reflect this change.
We conduct hearing tests, perform earwax removals, and fit & dispense hearing aids to our patients. We are a family owned practice in which the owner is the one who works directly with the patient. I have attached logos in various formats to use, as well as two ideas I found on this website; as well as a scanned copy of our current logo. Good luck!

Industry/Entity Type

Business

Contact Information for Business Card

Company name: Maplow Hearing Center
Provider name: Peter Mulvoy, Au.D. F/ISN
Phone number: (555) 318-6042
Address: 87 W. Linden Ave. Harlow Falls, OH 40981
email: maplowhearing@postvale.net
website: maplowhearing.com

Colors
000000
aaaaaa
dbdbdb
cacaca
9bcb3c
afd23c
cadf82
b1b1b1

Requirements
Must have
• My card must include information in the "details" section. In the attached images, I found a few that I liked and I would like to model after - "brisk tumblin'" and "Sound Wellness Center".
• Must be horizontal.
• Must include logos provided. I uploaded them in various file formats and various ways.
• Must match logo font, if possible, if not, please get as close as you can.
Nice to have
• I really like the idea of having a color on one side with just the logo and company name and the contact information and provider name on the other side. I also really like the idea of having the main color dominating on the logo/company side with accent of that same color on the contact side of the card.
Should not have
• Must not be vertical.

```html
<!DOCTYPE html>
<html lang="en">
<head>
<meta charset="UTF-8">
<title>Maplow Hearing Center – Business Card</title>
<link href="https://fonts.googleapis.com/css2?family=Cinzel:wght@400;500&family=Raleway:wght@300;400&family=Montserrat:wght@300;400&display=swap" rel="stylesheet">
<style>
  :root {
    --bg: #cacaca;
    --card: #252525;
    --card-edge: #1c1c1c;
    --green: #9bcb3c;
    --green-soft: #afd23c;
    --text-light: #dbdbdb;
    --text-muted: #b1b1b1;
  }
  * { margin: 0; padding: 0; box-sizing: border-box; }
  html, body { width: 1200px; height: 834px; overflow: hidden; }
  body {
    background: var(--bg);
    display: flex;
    align-items: center;
    justify-content: center;
    gap: 40px;
  }
  .card {
    position: relative;
    width: 540px;
    height: 309px;
    background: linear-gradient(160deg, #2b2b2b 0%, var(--card) 60%, var(--card-edge) 100%);
    box-shadow: 0 10px 30px rgba(0,0,0,0.35);
    overflow: hidden;
  }
  .brand {
    display: flex;
    align-items: center;
    gap: 12px;
  }
  .brand-dot {
    width: 14px;
    height: 14px;
    border-radius: 50%;
    background: var(--green);
    flex: none;
  }
  .brand-name {
    font-family: "Raleway", sans-serif;
    font-weight: 400;
    color: var(--text-light);
    text-transform: uppercase;
    letter-spacing: -0.5px;
    white-space: nowrap;
  }
  /* Front */
  .card-front .brand {
    position: absolute;
    left: 50%;
    top: 130px;
    transform: translateX(-50%);
  }
  .card-front .brand-name { font-size: 30px; }
  .web-tab {
    position: absolute;
    right: 40px;
    bottom: 0;
    width: 230px;
    height: 50px;
    background: var(--green);
    border-radius: 22px 22px 0 0;
    display: flex;
    align-items: center;
    justify-content: center;
    font-family: "Montserrat", sans-serif;
    font-weight: 400;
    font-size: 12px;
    color: #ffffff;
    letter-spacing: 0.3px;
  }
  /* Back */
  .card-back {
    display: flex;
    flex-direction: column;
    align-items: center;
    padding-top: 70px;
  }
  .card-back .brand-name { font-size: 27px; }
  .provider {
    margin-top: 18px;
    font-family: "Cinzel", serif;
    font-weight: 400;
    font-size: 18px;
    color: var(--green-soft);
    letter-spacing: 0.5px;
  }
  .divider {
    width: 150px;
    height: 1px;
    margin: 10px 0 12px;
    background: linear-gradient(90deg, transparent, var(--green), transparent);
  }
  .contact {
    list-style: none;
    text-align: center;
    font-family: "Montserrat", sans-serif;
    font-weight: 300;
    font-size: 11.5px;
    line-height: 1.75;
    color: var(--text-light);
  }
</style>
</head>
<body>
  <section class="card card-front" aria-label="Card front">
    <div class="brand">
      <span class="brand-dot"></span>
      <span class="brand-name">Maplow Hearing Center</span>
    </div>
    <div class="web-tab">www.maplowhearing.com</div>
  </section>

  <section class="card card-back" aria-label="Card back">
    <div class="brand">
      <span class="brand-dot"></span>
      <span class="brand-name">Maplow Hearing Center</span>
    </div>
    <p class="provider">Peter Mulvoy, Au.D. F/ISN</p>
    <div class="divider"></div>
    <ul class="contact">
      <li>87 W. Linden Ave. Harlow Falls, OH 40981</li>
      <li>(555) 318-6042</li>
      <li>maplowhearing@postvale.net</li>
      <li>www.maplowhearing.com</li>
    </ul>
  </section>
</body>
</html>
```